Law Office business card design

I have a general practice specializing in criminal defense work and domestic cases. I have extensive trial and appellate experience.

Target Market(s)

general public

Industry/Entity Type

Defense

Contact Information for Business Card

Dorrington Law Office, P.A.
382 N. 4th
PO Box 5284
Salina, KS 67409-5284
(785) 555-0172
(785) 555-0198 FAX
tdorrin@quellmail.net

Requirements
Must have
• A symbol that immediately identifes the card as a legal practice.

```html
<!DOCTYPE html>
<html lang="en">
<head>
<meta charset="utf-8">
<title>Dorrington Law Office, P.A. — Business Card</title>
<link rel="stylesheet" href="https://fonts.googleapis.com/css2?family=Source+Sans+3:wght@300;400&display=swap">
<style>
  :root {
    --card-base: #0b0b0c;
    --card-glow: #2a2b2d;
    --text-soft: #a4a5a7;
    --text-bright: #c2c3c5;
    --divider-dark: #050505;
    --divider-light: #3a3b3d;
    --emblem-light: #e4e4e4;
    --emblem-dark: #6d6d6d;
  }
  html, body {
    margin: 0;
    padding: 0;
    width: 1200px;
    height: 702px;
    overflow: hidden;
    background: var(--card-base);
  }
  .card {
    position: relative;
    width: 1200px;
    height: 702px;
    overflow: hidden;
    font-family: "Source Sans 3", sans-serif;
    color: var(--text-soft);
    background:
      radial-gradient(ellipse 520px 300px at 600px 330px, var(--card-glow) 0%, rgba(42,43,45,0.35) 55%, rgba(11,11,12,0) 100%),
      var(--card-base);
  }
  .emblem {
    position: absolute;
    left: 962px;
    top: 61px;
    width: 100px;
    height: 97px;
    border-radius: 6px;
    background: linear-gradient(180deg, var(--emblem-light) 0%, var(--emblem-dark) 100%);
  }
  .divider {
    position: absolute;
    left: 624px;
    top: 220px;
    width: 3px;
    height: 290px;
    background: linear-gradient(90deg, var(--divider-dark) 0 1px, var(--divider-light) 1px 2px, transparent 2px);
    opacity: 0.9;
  }
  .firm-name {
    position: absolute;
    right: 608px;
    top: 318px;
    margin: 0;
    font-size: 38px;
    font-weight: 300;
    letter-spacing: -2px;
    white-space: nowrap;
    color: var(--text-soft);
  }
  .firm-email {
    position: absolute;
    right: 608px;
    top: 378px;
    width: 420px;
    text-align: center;
    font-size: 19px;
    letter-spacing: 0.8px;
    color: var(--text-soft);
  }
  .monogram {
    position: absolute;
    left: 658px;
    top: 286px;
    margin: 0;
    font-size: 97px;
    font-weight: 400;
    letter-spacing: -3px;
    line-height: 1;
    color: var(--text-bright);
  }
  .contact-line {
    position: absolute;
    top: 609px;
    font-size: 20px;
    letter-spacing: 0.6px;
    white-space: nowrap;
    color: var(--text-soft);
  }
  .contact-address { left: 114px; }
  .contact-phone { left: 655px; }
  .contact-fax { left: 878px; }
</style>
</head>
<body>
  <div class="card">
    <div class="emblem" role="img" aria-label="Silver scales of justice emblem"></div>

    <h1 class="firm-name">Dorrington Law Office, P.A.</h1>
    <div class="firm-email">tdorrin@quellmail.net</div>

    <div class="divider"></div>

    <p class="monogram">Dor</p>

    <div class="contact-line contact-address">382 N. 4th PO Box 5284 Salina, KS 67409-5284</div>
    <div class="contact-line contact-phone">P: (785) 555-0172</div>
    <div class="contact-line contact-fax">F: (785) 555-0198</div>
  </div>
</body>
</html>
```